It's a new electrical company based in Newcastle NSW. I would like a logo between the two words "BRYN (insert logo) VOLT". I would like the logo to represent electrical and celtic style. For example I have seen a light bulb with a celtic pattern in the middle which looked very good. I would like it to be a white card, mainly black writing and quite basic not too much going on. But maybe have the logo partially red or green?

BRYN VOLT
Electrical Contractors
Domestic, commercial, fault finding, testing, re wires, switchboard upgrades
License No: 738421K
Fully Insured
Phone: 0431587720

```html
<!DOCTYPE html>
<html lang="en">
<head>
<meta charset="utf-8">
<title>Bryn Volt – Business Card</title>
<link href="https://fonts.googleapis.com/css2?family=Ubuntu:wght@400;500;700&display=swap" rel="stylesheet">
<style>
  :root {
    --stage: #e9e9e9;
    --card: #ffffff;
    --ink: #1b1b1b;
    --accent: #e3202a;
    --ghost: #ececec;
  }
  html, body {
    margin: 0;
    width: 1200px;
    height: 1000px;
    overflow: hidden;
    background: var(--stage);
    font-family: "Ubuntu", sans-serif;
  }
  .business-card {
    position: absolute;
    left: 100px;
    top: 210px;
    width: 1000px;
    height: 580px;
    background: var(--card);
    overflow: hidden;
    box-shadow: 0 10px 30px rgba(0,0,0,0.12);
  }
  .ghost-mark {
    position: absolute;
    left: -80px;
    top: -60px;
    width: 620px;
    height: 600px;
  }
  .brand {
    position: absolute;
    right: 50px;
    top: 48px;
    display: flex;
    align-items: center;
    gap: 24px;
    font-weight: 500;
    font-size: 66px;
    letter-spacing: 0.5px;
    color: var(--ink);
  }
  .brand-dot {
    width: 46px;
    height: 46px;
    border-radius: 50%;
    background: var(--accent);
  }
  .services {
    position: absolute;
    right: 50px;
    top: 165px;
    text-align: right;
    font-size: 19px;
    line-height: 1.15;
    color: var(--ink);
  }
  .services .lead { font-weight: 700; }
  .phone {
    position: absolute;
    right: 50px;
    bottom: 70px;
    font-size: 20px;
    font-weight: 700;
    color: var(--ink);
  }
  .licence {
    position: absolute;
    left: 40px;
    bottom: 40px;
    font-size: 22px;
    font-weight: 700;
    color: var(--ink);
  }
  .label { color: var(--accent); }
  .base-band {
    position: absolute;
    left: 0;
    right: 0;
    bottom: 0;
    height: 14px;
    background: var(--accent);
  }
</style>
</head>
<body>
  <section class="business-card">
    <svg class="ghost-mark" role="img" aria-label="Large faint brand symbol decoration" viewBox="0 0 620 600">
      <defs>
        <radialGradient id="ghost-fade" cx="50%" cy="45%" r="50%">
          <stop offset="0%" stop-color="var(--ghost)" stop-opacity="0.9"/>
          <stop offset="60%" stop-color="var(--ghost)" stop-opacity="0.5"/>
          <stop offset="100%" stop-color="var(--ghost)" stop-opacity="0"/>
        </radialGradient>
      </defs>
      <rect x="0" y="0" width="620" height="600" fill="url(#ghost-fade)"/>
    </svg>

    <div class="brand">
      <span class="brand-name">BRYN</span>
      <span class="brand-dot"></span>
      <span class="brand-name">VOLT</span>
    </div>

    <div class="services">
      <div class="lead">BRYN VOLT Electrical Contractors Domestic</div>
      <div>commercial - fault finding - testing</div>
      <div>re wires - switchboard upgrades</div>
    </div>

    <div class="phone"><span class="label">Phone:</span> 043 15 87 720</div>
    <div class="licence"><span class="label">License No:</span> 738421K Fully Insured</div>

    <div class="base-band"></div>
  </section>
</body>
</html>
```